Original catchy book cover

I need a book cover for my book "The Copper Kettle Handbook" (https://quillpress.example/copperkettle). This will be a book self published on marketvale.
The book talks about the following concepts:
- Iterative product delivery
- Early discovery using feedback from customers
- Start small, think big, move fast
- Slice the product into valuable increments that can be validated with customers
- Experimental approach to deciding the next slice of work
A simple cover that stands out from the business books already out there! Some examples are:
https://www.marketvale.example/Tide-Harbor-Steady-Teams-Quietly-ebook/dp/X00AAA1111/ref=sr_1_1?ie=UTF8&qid=1000000001&sr=8-1&keywords=tide+and+harbor
https://www.marketvale.example/Copper-Kettle-Almanac-Brew-Ideas-ebook/dp/X00BBB2222/ref=sr_1_1?s=digital-text&ie=UTF8&qid=1000000002&sr=1-1&keywords=copper+kettle+almanac
https://www.marketvale.example/Orchard-Paths-Rewoven-Compass-Fogbanks-ebook/dp/X00CCC3333/ref=pd_sim_351_2?_encoding=UTF8&psc=1&refRID=ZZZZZZZZZZZZZZZZZZZZ
Lastly, attached are 2 draft covers that i've been playing with. Would love a graphic as part of the cover if it makes sense in your design! The graphic should tie to the meaning or themes of the book. Emphasis on ways of working, collaboration, experimentation, hypothesis, agile, incremental or adaptive. Those are some words that describe the content of the book.
Alternatively, something abstract could also be an option if a literal graphic doesn't suit the theme of your design.
Target Market(s)
Product owners, scrum masters, people in the agile community, software developers, designers
Industry/Entity Type
Information Technology
Font styles to use
Colors
Designer to choose colors to be used in the design.
Requirements
Must have
- Title, Subtitle, Author Name
- Back of the book should have space for a description (use lorem ipsum for now)
- Please use the editorial logo
- (please omit "created by Tomas Verhelst" because the editorial logo replaces that.
- The design must be original art or graphics (i.e. it should be similar to another cover in this topic).
Nice to have
- A graphic would be ideal if it is relevant to the book topic, otherwise a nice simple cover that uses colors or patterns that are easy to recall.
- The color suggestions below are suggestions only. Do not feel you have to incorporate all the colors and feel free to recommend an alternate palette.
Should not have
- Clipart or generic stock art photos. Images for the sake of images, traditional logos (e.g. a computer, a phone etc unless it's part of an overall theme that ties the logos together).

```html
<!DOCTYPE html>
<html lang="en">
<head>
<meta charset="utf-8">
<title>The Copper Kettle Handbook — Cover</title>
<link rel="stylesheet" href="https://fonts.googleapis.com/css2?family=Caveat+Brush&family=Roboto:wght@400;500;700&family=Roboto+Condensed:wght@700&display=swap">
<style>
  :root {
    --navy-core: #0d5676;
    --navy-mid: #0a4462;
    --navy-edge: #083149;
    --chalk: #ffffff;
    --chalk-soft: rgba(255, 255, 255, 0.16);
    --signal-red: #e43a2b;
    --signal-red-soft: rgba(228, 58, 43, 0.32);
    --publisher-orange: #ec6a2c;
  }
  * { margin: 0; padding: 0; box-sizing: border-box; }
  html, body { width: 800px; height: 1200px; overflow: hidden; background: var(--navy-edge); }
  .cover {
    position: relative;
    width: 800px;
    height: 1200px;
    overflow: hidden;
    background: radial-gradient(ellipse 70% 60% at 50% 48%, var(--navy-core) 0%, var(--navy-mid) 55%, var(--navy-edge) 100%);
    font-family: "Roboto", Arial, sans-serif;
    color: var(--chalk);
  }
  .subtitle {
    position: absolute;
    left: 30px;
    top: 56px;
    width: 740px;
    height: 26px;
  }
  .subtitle text {
    font-family: "Roboto Condensed", "Arial Narrow", sans-serif;
    font-weight: 700;
    font-size: 21px;
    fill: var(--signal-red);
  }
  .cycle-sketch {
    position: absolute;
    border-radius: 60px;
    background: linear-gradient(135deg, rgba(255,255,255,0.05), var(--chalk-soft), rgba(255,255,255,0.05));
  }
  .cycle-sketch.top-left { left: 34px; top: 140px; width: 276px; height: 226px; border-radius: 220px 40px 40px 40px; }
  .cycle-sketch.top-right { left: 504px; top: 136px; width: 250px; height: 248px; border-radius: 40px 220px 40px 40px; }
  .cycle-sketch.bottom-right { left: 434px; top: 758px; width: 318px; height: 170px; border-radius: 40px 40px 200px 40px; }

  .title-block { position: absolute; left: 0; width: 800px; text-align: center; display: block; }
  .title-the {
    top: 234px;
    font-size: 46px;
    font-weight: 400;
    line-height: 56px;
  }
  .title-main {
    font-family: "Caveat Brush", "Comic Sans MS", cursive;
    font-weight: 400;
    font-size: 172px;
    line-height: 170px;
    letter-spacing: 2px;
    text-transform: uppercase;
  }
  .title-main.line-one { top: 312px; }
  .title-main.line-two { top: 486px; }
  .title-last {
    top: 690px;
    font-size: 80px;
    font-weight: 400;
    line-height: 90px;
  }
  .sketch-mark {
    position: absolute;
    left: 76px;
    top: 760px;
    width: 134px;
    height: 134px;
    border-radius: 50%;
    background: radial-gradient(circle, rgba(228,58,43,0.08) 0%, var(--signal-red-soft) 80%, rgba(228,58,43,0.12) 100%);
  }
  .authors {
    position: absolute;
    left: 78px;
    top: 1018px;
    font-size: 38px;
    font-weight: 400;
    line-height: 66px;
    text-transform: uppercase;
    white-space: nowrap;
  }
  .publisher {
    position: absolute;
    left: 444px;
    top: 1026px;
    display: flex;
    align-items: center;
    gap: 24px;
    color: var(--publisher-orange);
    font-weight: 500;
  }
  .publisher-dot {
    width: 84px;
    height: 84px;
    border-radius: 50%;
    background: var(--publisher-orange);
    flex: none;
  }
  .publisher-name { font-size: 30px; line-height: 31px; }
  .publisher-site { font-size: 22px; line-height: 28px; }
</style>
</head>
<body>
<main class="cover">
  <svg class="subtitle" viewBox="0 0 740 26" aria-label="A practitioner's guide to building products customers love">
    <text x="0" y="21" textLength="740" lengthAdjust="spacingAndGlyphs">A PRACTITIONER’S GUIDE TO BUILDING PRODUCTS CUSTOMERS LOVE</text>
  </svg>

  <div class="cycle-sketch top-left" role="img" aria-label="Hand-drawn chalk arrow curving up to the right"></div>
  <div class="cycle-sketch top-right" role="img" aria-label="Hand-drawn chalk arrow curving down the right side"></div>
  <div class="cycle-sketch bottom-right" role="img" aria-label="Hand-drawn chalk arrow curving back to the left"></div>

  <h1>
    <span class="title-block title-the">THE</span>
    <span class="title-block title-main line-one">Copper</span>
    <span class="title-block title-main line-two">Kettle</span>
    <span class="title-block title-last">HANDBOOK</span>
  </h1>

  <div class="sketch-mark" role="img" aria-label="Red hand-drawn sketch"></div>

  <div class="authors">
    <p>Maren Solberg</p>
    <p>Tomas Verhelst</p>
  </div>

  <div class="publisher">
    <span class="publisher-dot"></span>
    <div>
      <p class="publisher-name">Editora<br>Solano</p>
      <p class="publisher-site">solano.example</p>
    </div>
  </div>
</main>
</body>
</html>
```